Cover Page for Financial Statements

We need a cover page designed for our Financial Statements. It will need to include our business logo and the Chartered accountant logo.
We have included our current title page ( image titled full.png ) to show all the information that is needed to be included such as the title 'Financial Statements' and 'The year ended March 2023'. We would like to see designs that reflect our logo but also adds some interest with objects / deisngs that fill up more of the page.

Industry/Entity Type

Accounting

Font styles to use
Serif
Sans Serif

Colors

Designer to choose only greyscale colors for use in the design.

Requirements
Must have
• - A4 document size, our logo, Chartered Accountant Logo
Should not have
• Bright Colors

```html
<!DOCTYPE html>
<html lang="en">
<head>
<meta charset="utf-8">
<title>Tidemark Accounting &amp; Advisory — 2023 Financial Statements</title>
<link rel="stylesheet" href="https://fonts.googleapis.com/css2?family=Inter:wght@400;700&display=swap">
<style>
  :root {
    --backdrop: #d9dadc;
    --paper: #ffffff;
    --ink: #231f20;
    --ink-soft: #3a3a3a;
    --photo-light: #f4f4f4;
    --photo-mid: #c9c9c9;
    --photo-dark: #6e6e6e;
  }
  * { margin: 0; padding: 0; box-sizing: border-box; }
  html, body {
    width: 1200px; height: 1200px; overflow: hidden;
    background: var(--backdrop);
    font-family: "Inter", "Helvetica Neue", Arial, sans-serif;
    color: var(--ink);
  }
  .cover {
    position: absolute; left: 261px; top: 120px;
    width: 678px; height: 960px;
    background: var(--paper);
  }
  .brand {
    position: absolute; left: 135px; top: 92px; width: 404px;
    text-align: center; font-weight: 700; color: var(--ink);
  }
  .brand__name { font-size: 54px; letter-spacing: 6px; line-height: 1; }
  .brand__tag { font-size: 15px; letter-spacing: 5.5px; margin-top: 14px; }
  .cover__title {
    position: absolute; left: 0; width: 678px; top: 312px;
    text-align: center; font-size: 22px; font-weight: 700; letter-spacing: 0.2px;
  }
  .cover__recipient {
    position: absolute; left: 185px; top: 375px;
    font-size: 12.5px; font-weight: 400; color: var(--ink-soft);
  }
  .cover__photo {
    position: absolute; left: 25px; top: 476px; width: 628px; height: 364px;
    background:
      linear-gradient(to bottom, var(--paper) 0%, rgba(255,255,255,0) 22%),
      linear-gradient(135deg, var(--photo-light) 0%, var(--photo-mid) 45%, var(--photo-dark) 70%, var(--photo-mid) 100%);
  }
  .footer-frame { position: absolute; left: 0; top: 0; width: 678px; height: 960px; pointer-events: none; }
  .offices {
    position: absolute; left: 42px; top: 857px;
    font-size: 9.3px; line-height: 16px; color: var(--ink);
  }
  .offices strong { font-weight: 700; }
  .services {
    position: absolute; left: 42px; top: 901px;
    font-size: 9.4px; line-height: 14px; color: var(--ink-soft); text-transform: uppercase;
  }
  .partner-badge { position: absolute; left: 570px; top: 858px; width: 40px; height: 40px; }
</style>
</head>
<body>
  <main class="cover">
    <div class="brand">
      <div class="brand__name">TIDEMARK</div>
      <div class="brand__tag">ACCOUNTING &amp; ADVISORY</div>
    </div>

    <h1 class="cover__title">2023 Financial Statements</h1>
    <p class="cover__recipient">Prepared for: . . . . . . . . . . . . . . . . . . . . . . . . . . . . . . . . . . . . . . . .</p>

    <div class="cover__photo" role="img" aria-label="Photograph of colleagues at a meeting table reviewing printed financial charts and reports, in soft greyscale"></div>

    <svg class="footer-frame" viewBox="0 0 678 960" aria-hidden="true">
      <g stroke="var(--ink)" stroke-width="1.2" fill="none">
        <polyline points="255,846 651,846 651,911"/>
        <polyline points="25.5,869 25.5,933 200,933"/>
        <line x1="42" y1="895" x2="519" y2="895" stroke-width="0.8"/>
      </g>
    </svg>

    <div class="offices">
      <div><strong>HARBOUR OFFICE:</strong> 18 Quayside Lane, Westhaven, 5041&nbsp; <strong>Ph:</strong> 04 555 0182</div>
      <div><strong>BAYSIDE OFFICE:</strong> 47 Shoreline Parade, Kelby, 5073&nbsp; <strong>Ph:</strong> 04 555 0367</div>
    </div>

    <div class="services">
      <div>• Tax &amp; Accounting Services &nbsp;• &nbsp;Business Advice &nbsp;• &nbsp;Business Structures &nbsp;• &nbsp;Cloud Software &amp; Other</div>
      <div>• &nbsp;Business Start-ups &nbsp;• &nbsp;Tax Debt and Other Services</div>
    </div>

    <svg class="partner-badge" viewBox="0 0 40 40" role="img" aria-label="Professional accreditation badge">
      <circle cx="20" cy="20" r="18" fill="var(--ink)"/>
    </svg>
  </main>
</body>
</html>
```